I am a pastry chef and just started my own business. I make all sorts of pastries: french macarons, petit fours, artisan chocolates, artisan bread, and they can be ordered on the website. I'm obsessed with Wonderland, so I'd like to have a logo & a background that incorporate that, something whimsical. I was thinking of a white rabbit wearing a chef toque - maybe he could have a monocle on. The logo could go on one side of the business card with "Tiny Baker of Moonbrook" on a banner of some sort at the bottom, and the contact & info could go on the other side. I'd like a really light color as the background, maybe a really light yellow.

Industry/Entity Type

Chef

Contact Information for Business Card

Tiny Baker of Moonbrook
Mira Delsan Corwick
tinybakerofmoonbrook.shopveltra.com
tinybakerofmoonbrook@mailquor.com
514-83-2071

```html
<!DOCTYPE html>
<html lang="en">
<head>
<meta charset="utf-8">
<title>Tiny Baker of Moonbrook – Business Card</title>
<link href="https://fonts.googleapis.com/css2?family=Chewy&family=Caprasimo&family=Jost:wght@400&display=swap" rel="stylesheet">
<style>
  :root {
    --page: #ffffff;
    --band: #ffff00;
    --field: #f1fc5f;
    --wave-line: #ffffff;
    --wave-shadow: rgba(120, 120, 0, 0.35);
    --ink: #0d0d0d;
    --icon-dot: #ffff00;
  }
  * { margin: 0; padding: 0; box-sizing: border-box; }
  html, body {
    width: 849px;
    height: 1200px;
    overflow: hidden;
    background: var(--page);
  }
  .sheet {
    position: relative;
    width: 849px;
    height: 1200px;
  }
  .card {
    position: absolute;
    left: 103px;
    width: 643px;
    height: 377px;
    border-radius: 26px;
    overflow: hidden;
    background: var(--field);
    box-shadow: 0 8px 22px rgba(0, 0, 0, 0.18), 0 2px 6px rgba(0, 0, 0, 0.08);
  }
  .card--front { top: 168px; }
  .card--back { top: 683px; }
  .card__waves {
    position: absolute;
    inset: 0;
    width: 100%;
    height: 100%;
  }
  .brand-title {
    position: absolute;
    left: 0;
    right: 0;
    top: 128px;
    text-align: center;
    font-family: "Chewy", "Comic Sans MS", cursive;
    font-size: 58px;
    line-height: 59px;
    letter-spacing: 3px;
    text-transform: uppercase;
    color: var(--ink);
  }
  .front-url {
    position: absolute;
    left: 0;
    right: 0;
    top: 329px;
    text-align: center;
    font-family: "Jost", "Helvetica", sans-serif;
    font-size: 19px;
    letter-spacing: 1.2px;
    color: var(--ink);
  }
  .person-name {
    position: absolute;
    left: 50px;
    top: 127px;
    font-family: "Caprasimo", "Cooper Black", serif;
    font-size: 28px;
    letter-spacing: 0.5px;
    color: var(--ink);
  }
  .contact-list {
    position: absolute;
    left: 260px;
    top: 198px;
    list-style: none;
    font-family: "Jost", "Helvetica", sans-serif;
    font-size: 19px;
    line-height: 26px;
    color: var(--ink);
  }
  .contact-list li {
    display: flex;
    align-items: center;
  }
  .contact-icon {
    width: 16px;
    height: 16px;
    margin-right: 13px;
    flex: none;
  }
</style>
</head>
<body>
<main class="sheet">

  <section class="card card--front" aria-label="Card front">
    <svg class="card__waves" viewBox="0 0 643 377" preserveAspectRatio="none" aria-hidden="true">
      <defs>
        <filter id="waveShadowFront" x="-5%" y="-50%" width="110%" height="200%">
          <feDropShadow dx="0" dy="4" stdDeviation="3" flood-color="#7a7a00" flood-opacity="0.35"/>
        </filter>
      </defs>
      <path d="M0 0 H643 V66 C480 62 300 54 170 52 C100 51 40 53 0 56 Z" fill="var(--band)" filter="url(#waveShadowFront)"/>
      <path d="M0 58 C40 55 100 53 170 54 C300 56 480 64 643 68" fill="none" stroke="var(--wave-line)" stroke-width="4"/>
      <path d="M0 377 V306 C80 302 180 299 300 300 C430 302 540 310 643 318 V377 Z" fill="var(--band)" filter="url(#waveShadowFront)"/>
      <path d="M0 311 C80 306 180 303 300 304 C430 306 540 314 643 322" fill="none" stroke="var(--wave-line)" stroke-width="4"/>
    </svg>
    <h1 class="brand-title">Tiny Baker of<br>Moonbrook</h1>
    <p class="front-url">tinybakerofmoonbrook.shopveltra.com</p>
  </section>

  <section class="card card--back" aria-label="Card back">
    <svg class="card__waves" viewBox="0 0 643 377" preserveAspectRatio="none" aria-hidden="true">
      <defs>
        <filter id="waveShadowBack" x="-5%" y="-50%" width="110%" height="200%">
          <feDropShadow dx="0" dy="4" stdDeviation="3" flood-color="#7a7a00" flood-opacity="0.35"/>
        </filter>
      </defs>
      <path d="M0 0 H643 V64 C480 60 300 54 170 52 C100 51 40 52 0 54 Z" fill="var(--band)" filter="url(#waveShadowBack)"/>
      <path d="M0 56 C40 54 100 53 170 54 C300 56 480 62 643 66" fill="none" stroke="var(--wave-line)" stroke-width="4"/>
      <path d="M0 377 V303 C80 299 180 297 300 298 C430 300 540 306 643 312 V377 Z" fill="var(--band)" filter="url(#waveShadowBack)"/>
      <path d="M0 308 C80 303 180 301 300 302 C430 304 540 310 643 316" fill="none" stroke="var(--wave-line)" stroke-width="4"/>
    </svg>
    <h2 class="person-name">Mira Delsan Corwick</h2>
    <ul class="contact-list">
      <li>
        <svg class="contact-icon" viewBox="0 0 16 16" aria-hidden="true">
          <circle cx="8" cy="8" r="8" fill="var(--icon-dot)"/>
          <path d="M5.3 3.8 L6.6 3.6 L7.3 5.6 L6.5 6.3 C6.9 7.4 7.7 8.3 8.8 8.8 L9.5 8 L11.5 8.7 L11.3 10 C10.9 10.6 10.2 10.8 9.5 10.6 C7.4 9.9 5.9 8.4 5.2 6.3 C5 5.6 5 4.3 5.3 3.8 Z" fill="var(--ink)"/>
        </svg>
        <span>514-83-2071</span>
      </li>
      <li>
        <svg class="contact-icon" viewBox="0 0 16 16" aria-hidden="true">
          <circle cx="8" cy="8" r="8" fill="var(--icon-dot)"/>
          <rect x="4" y="5.2" width="8" height="5.6" rx="0.6" fill="var(--ink)"/>
          <path d="M4.3 5.6 L8 8.3 L11.7 5.6" fill="none" stroke="var(--icon-dot)" stroke-width="0.9"/>
        </svg>
        <span>tinybakerofmoonbrook@mailquor.com</span>
      </li>
      <li>
        <svg class="contact-icon" viewBox="0 0 16 16" aria-hidden="true">
          <circle cx="8" cy="8" r="8" fill="var(--icon-dot)"/>
          <circle cx="8" cy="8" r="4.3" fill="var(--ink)"/>
          <path d="M3.7 8 H12.3 M8 3.7 V12.3 M5 5.6 H11 M5 10.4 H11" stroke="var(--icon-dot)" stroke-width="0.7" fill="none"/>
          <ellipse cx="8" cy="8" rx="1.8" ry="4.3" fill="none" stroke="var(--icon-dot)" stroke-width="0.7"/>
        </svg>
        <span>tinybakerofmoonbrook.shopveltra.com</span>
      </li>
    </ul>
  </section>

</main>
</body>
</html>
```